Savour and Thrive Wellbeing is being Launched and needs a business card and stationery package

I need a stationery package including business card (primary focus) , letterhead, digital letterhead, envelopes, with compliments slip, A 5 note sheet for the rebranding of my business and launch of my new website. I have a logo, like beige, brown earthy tones with a hint of red. I would also like the option of my letterhead also being printed on recycled paper in another format as well as the traditional letterhead. I do also send my letters to GPs and specialists digitally as well. I like to stand out from the usual stereotype of fruits and vegetables on business cards as I find that quite tacky and stereotypical. I want the business card to capture the essence of my logo as natural, nutrition, enjoyment, nurturing and freedom with food. I have attached the logo, and additional brief sheet on my ideas. Happy to have any background that is complementary to my theme, and what you believe would be catching. Definitely DONT'T like pink, try to pick up the darker colour in the logo please. and think too much black is a little overpowering.

Target Market(s)

clients who are interested in improving their health and wellness. Client 80% females; 20% males

Industry/Entity Type

Health And Wellness

Contact Information for Business Card

I am open to having different backgrounds as well that would complement the logo. Probably less emphasis on the heart out of the logo - just happy to keep that in the logo only please
I am also wanting two business cards - one for the appointments, one for general distribution and media distribution (both need to look consistent though) - but does give opportunity for one of the business cards to be less wordy and more striking. And the front of the business card can certainly stand out with the entire savour and thrive logo and my name and grab the attention of the receiver.
1st business card
on front:
Lorena Whitcombe
Savour and Thrive Wellbeing & logo
Nutritionist and Dietitian
Tarvel Medical Centre
647 Brindle Hill Rd, Quorrel Q 4987
Phone: (07) 3017 2968 Fax: (07) 3156 7209
Mobile: 0400 261 937
www.savourandthrivewellbeing.example.au
lorena@savourandthrivewellbeing.example.au
on back:
next appointment

……………………….. at ……………………… (possibly 4 times)
If you are unable to keep your appointment, please contact us as soon as possible (small font)
2nd business card (needs to be very eye catching and stand out)
on front: Savour and Thrive Wellbeing logo and my name
on back:
Lorena Whitcombe
address
phones, fax, website, email address

Font styles to use
Other font styles liked:
• please refer to logo

Requirements
Must have
• refreshing and simple; new and vibrant - I am rebranding my business after 20 years
• to get a feel of what is the theme - go to my new website (not completed as yet - but you will get a preliminary view) - don't do as google search as blocked - but can put into website header and it will be shown
• www.savourandthrivewellbeing.example.au - but please ignore the colouring of the 4 blocks under the slider on the home page - I am not wanting these colourings - they are getting updated.
Nice to have
• earthy tones, beige, hint of red, fonts to match logo if possible, organic, modern
• get inspiration from my logo please, open to having other backgrounds that complement
Should not have
• no food shots or stereotypical weight/ scales images
• no green, yellow or orange

```html
<!DOCTYPE html>
<html lang="en">
<head>
<meta charset="utf-8">
<title>Savour and Thrive Wellbeing – Business Card</title>
<link href="https://fonts.googleapis.com/css2?family=Arimo:wght@400;700&family=Crimson+Text:ital@1&display=swap" rel="stylesheet">
<style>
  :root {
    --page: #d8d2c6;
    --beige: #e4d6b1;
    --maroon: #a23a58;
    --maroon-dark: #8c2f4b;
    --ink: #3b2d2a;
    --white: #ffffff;
  }
  * { box-sizing: border-box; margin: 0; padding: 0; }
  html, body { width: 1200px; height: 950px; overflow: hidden; }
  body {
    background: var(--page);
    font-family: "Arimo", Arial, sans-serif;
    position: relative;
  }
  .card {
    position: absolute;
    left: 250px;
    width: 700px;
    height: 428px;
    background: var(--beige);
    overflow: hidden;
    box-shadow: 0 6px 18px rgba(60, 40, 30, 0.25);
  }
  .card--front { top: 35px; }
  .card--back { top: 487px; }
  .card__art { position: absolute; inset: 0; width: 100%; height: 100%; }

  /* Front */
  .brand {
    position: absolute;
    top: 50px;
    right: 70px;
    display: flex;
    align-items: center;
    gap: 14px;
  }
  .brand__dot {
    width: 22px; height: 22px;
    border-radius: 50%;
    background: var(--maroon);
  }
  .brand__name {
    font-size: 30px;
    font-weight: 400;
    color: var(--ink);
    line-height: 1.15;
    width: 270px;
  }
  .contact {
    position: absolute;
    left: 42px;
    top: 186px;
    color: var(--white);
  }
  .contact__name { font-size: 24px; font-weight: 700; line-height: 1.15; }
  .contact__role { font-size: 15px; line-height: 1.2; margin-bottom: 10px; }
  .contact__line { font-size: 13px; line-height: 1.35; }

  /* Back */
  .appointment__title {
    position: absolute;
    top: 46px;
    right: 52px;
    color: var(--maroon);
    font-weight: 700;
    font-size: 20px;
    letter-spacing: 1px;
  }
  .appointment__rows {
    position: absolute;
    top: 100px;
    left: 70px;
    right: 52px;
  }
  .appointment__row {
    display: flex;
    align-items: flex-end;
    gap: 8px;
    height: 48px;
    font-size: 15px;
    color: var(--ink);
  }
  .appointment__blank { border-bottom: 2px dotted var(--ink); height: 1px; }
  .appointment__blank--day { flex: 0 0 340px; }
  .appointment__blank--time { flex: 1; }
  .appointment__note {
    position: absolute;
    left: 40px;
    bottom: 26px;
    color: var(--white);
    font-family: "Crimson Text", Georgia, serif;
    font-style: italic;
    font-size: 16px;
  }
</style>
</head>
<body>

<section class="card card--front" aria-label="Business card front">
  <svg class="card__art" viewBox="0 0 700 428" aria-hidden="true">
    <path d="M0,95 C260,112 500,175 700,285 C490,192 250,128 0,111 Z" fill="var(--maroon)"/>
    <path d="M0,127 C260,145 500,210 700,315 L700,428 L0,428 Z" fill="var(--maroon)"/>
  </svg>
  <div class="brand">
    <span class="brand__dot"></span>
    <span class="brand__name">Savour and Thrive Wellbeing</span>
  </div>
  <div class="contact">
    <h1 class="contact__name">Lorena Whitcombe</h1>
    <p class="contact__role">Nutritionist and Dietitian</p>
    <p class="contact__line">Tarvel Medical Centre</p>
    <p class="contact__line">647 Brindle Hill Rd</p>
    <p class="contact__line">Quorrel Q 4987</p>
    <p class="contact__line">P : (07) 3017 2968</p>
    <p class="contact__line">F : (07) 3156 7209</p>
    <p class="contact__line">M : 0400 261 937</p>
    <p class="contact__line">lorena@savourandthrivewellbeing.example.au</p>
    <p class="contact__line">www.savourandthrivewellbeing.example.au</p>
  </div>
</section>

<section class="card card--back" aria-label="Business card back">
  <svg class="card__art" viewBox="0 0 700 428" aria-hidden="true">
    <path d="M0,306 C260,296 500,322 700,384 C500,340 260,318 0,320 Z" fill="var(--maroon)"/>
    <path d="M0,334 C260,324 500,352 700,410 L700,428 L0,428 Z" fill="var(--maroon)"/>
  </svg>
  <h2 class="appointment__title">NEXT APPOINTMENT</h2>
  <div class="appointment__rows">
    <div class="appointment__row"><span class="appointment__blank appointment__blank--day"></span>at<span class="appointment__blank appointment__blank--time"></span></div>
    <div class="appointment__row"><span class="appointment__blank appointment__blank--day"></span>at<span class="appointment__blank appointment__blank--time"></span></div>
    <div class="appointment__row"><span class="appointment__blank appointment__blank--day"></span>at<span class="appointment__blank appointment__blank--time"></span></div>
    <div class="appointment__row"><span class="appointment__blank appointment__blank--day"></span>at<span class="appointment__blank appointment__blank--time"></span></div>
  </div>
  <p class="appointment__note">If you are unable to keep your appointment, please contact us as soon as possible</p>
</section>

</body>
</html>
```